Welcome Center Signage/logo Design with Multicultural Relevance

We are looking to have a welcome signage/logo designed for our church lobby with either the word "welcome" or "Welcome to the Dunmore Valley Fellowship!"

This design must include our organizational logo (attached). It could (but does not need to) also include our church vision: "Our vision is to be a thriving diverse urban church sharing Christ's love and serving the needs of our local and global communities." The logo/signage will be printed on 4' x 6' stretch fabric.

This signage will then be hung up behind our welcome center...it will be one of the first things people see upon entering our building.

We are an urban multicultural church that has significant outreach into our local community, one that is quite culturally diverse. If you would like more information about our church, please visit www.dunmorevalleyfc.org.
Updates

Project Deadline Extended
Reason: We have committed to continue work with the designers on designs submitted over the last several days, and are scheduling the additional time needed to do so. Thank you!

Target Market(s)

Culturally (African American, Hispanic American, Asian American, European American) diverse millennials and iGens

Industry/Entity Type

Church

Font styles to use
Sans Serif

Requirements
Must have
• Our logo
Nice to have
• "Welcome" in many languages
Should not have
• I can't think of anything at the moment.

```html
<!DOCTYPE html>
<html lang="en">
<head>
<meta charset="utf-8">
<title>Dunmore Valley Fellowship – Welcome Banner</title>
<link rel="stylesheet" href="https://fonts.googleapis.com/css2?family=Quicksand:wght@300;700&family=Raleway:wght@200&family=Noto+Sans+KR:wght@300&display=swap">
<style>
  :root {
    --page: #ffffff;
    --blue-top: #2286cb;
    --blue-mid: #00adec;
    --blue-bottom: #0a76c0;
    --ink: #ffffff;
    --ink-soft: rgba(255,255,255,0.78);
    --ink-faint: rgba(255,255,255,0.6);
  }
  html, body {
    margin: 0;
    width: 1059px;
    height: 1200px;
    overflow: hidden;
    background: var(--page);
  }
  .canvas {
    position: relative;
    width: 1059px;
    height: 1200px;
  }
  .banner {
    position: absolute;
    left: 275px;
    top: 239px;
    width: 497px;
    height: 746px;
    overflow: hidden;
    display: block;
  }
  .frame-line { stroke: var(--ink); stroke-width: 2.5; fill: none; }
  .greeting {
    font-family: "Raleway", sans-serif;
    font-weight: 200;
    fill: var(--ink-soft);
  }
  .greeting--korean {
    font-family: "Noto Sans KR", sans-serif;
    font-weight: 300;
    fill: var(--ink-faint);
  }
  .greeting--main {
    font-family: "Quicksand", sans-serif;
    font-weight: 700;
    fill: var(--ink);
  }
  .church-name {
    font-family: "Quicksand", sans-serif;
    font-weight: 700;
    fill: var(--ink);
  }
</style>
</head>
<body>
<div class="canvas">
  <svg class="banner" viewBox="0 0 497 746" xmlns="http://www.w3.org/2000/svg" role="img" aria-label="Welcome banner for Dunmore Valley Fellowship">
    <defs>
      <linearGradient id="banner-fill" x1="0" y1="0" x2="0" y2="1">
        <stop offset="0" stop-color="var(--blue-top)"/>
        <stop offset="0.55" stop-color="var(--blue-mid)"/>
        <stop offset="1" stop-color="var(--blue-bottom)"/>
      </linearGradient>
    </defs>

    <rect class="banner-background" width="497" height="746" fill="url(#banner-fill)"/>

    <!-- frame lines running through the emblem -->
    <path class="frame-line" d="M121 0 V262"/>
    <path class="frame-line" d="M372 262 V746"/>
    <circle class="frame-line emblem-ring" cx="249" cy="259" r="123"/>

    <!-- church name in the emblem -->
    <text class="church-name" x="249" y="250" font-size="25" text-anchor="middle" textLength="190" lengthAdjust="spacingAndGlyphs">DUNMORE VALLEY</text>
    <text class="church-name" x="249" y="284" font-size="25" text-anchor="middle" textLength="150" lengthAdjust="spacingAndGlyphs">FELLOWSHIP</text>

    <!-- greetings above -->
    <text class="greeting greeting--korean" x="143" y="29" font-size="38" textLength="212" lengthAdjust="spacingAndGlyphs">환영합니다</text>
    <text class="greeting" x="143" y="75" font-size="38" textLength="212" lengthAdjust="spacingAndGlyphs">VÄLKOMMEN</text>
    <text class="greeting greeting--main" x="143" y="123" font-size="46" textLength="212" lengthAdjust="spacingAndGlyphs">WELCOME</text>

    <!-- greetings below -->
    <text class="greeting" x="143" y="441" font-size="38" textLength="212" lengthAdjust="spacingAndGlyphs">ISTEN HOZOTT</text>
    <text class="greeting" x="143" y="484" font-size="38" textLength="212" lengthAdjust="spacingAndGlyphs">BIENVENIDOS</text>
    <text class="greeting" x="143" y="527" font-size="38" textLength="212" lengthAdjust="spacingAndGlyphs">DOBRODOŠLI</text>
    <text class="greeting" x="143" y="576" font-size="58" textLength="212" lengthAdjust="spacingAndGlyphs">WELKOM</text>
    <text class="greeting" x="143" y="619" font-size="58" textLength="212" lengthAdjust="spacingAndGlyphs">KARIBUNI</text>
    <text class="greeting" x="143" y="656" font-size="45" textLength="212" lengthAdjust="spacingAndGlyphs">VELKOMMEN</text>
    <text class="greeting" x="143" y="699" font-size="38" textLength="212" lengthAdjust="spacingAndGlyphs">HOAN NGHINH</text>
    <text class="greeting" x="143" y="745" font-size="52" textLength="212" lengthAdjust="spacingAndGlyphs">BIENVENUE</text>
  </svg>
</div>
</body>
</html>
```